Tranquilly Balanced Restoration

We want to design a business card that is modern and appealing for an innovative psychedelic telemedicine company that provides at-home ketamine-assisted therapy along with wellness, longevity, and anti-aging medicines. We want to use our deep purple and white plus other colors you can find on our website. We don't have any strict brand guidelines yet so feel free to get creative. We want a very professional, but technology first modern design that will instill trust, peace, calm, but also be attractive to investors in the healthcare and SaaS space.

```html
<!DOCTYPE html>
<html lang="en">
<head>
<meta charset="utf-8">
<title>Tranquilly Balanced Restoration – Business Card</title>
<link rel="stylesheet" href="https://fonts.googleapis.com/css2?family=Fira+Sans:wght@400&family=Montserrat:wght@400;500;700&display=swap">
<style>
  :root {
    --stage: #7a5ca8;
    --deep-purple: #2c1a3e;
    --brand-purple: #7c64aa;
    --soft-purple: #9a88c0;
    --white: #ffffff;
    --ink: #1a1a1a;
  }
  * { margin: 0; padding: 0; box-sizing: border-box; }
  html, body {
    width: 1200px;
    height: 1000px;
    overflow: hidden;
    background: var(--stage);
  }
  .card {
    position: absolute;
    left: 261px;
    width: 676px;
    height: 386px;
    overflow: hidden;
  }
  .card--front { top: 83px; background: var(--deep-purple); }
  .card--back  { top: 537px; background: var(--white); font-family: "Montserrat", sans-serif; color: var(--ink); }

  .front-brand {
    position: absolute;
    left: 0; right: 0; top: 162px;
    display: flex;
    align-items: center;
    justify-content: center;
    gap: 16px;
  }
  .front-brand__dot {
    width: 30px; height: 30px;
    border-radius: 50%;
    background: var(--white);
  }
  .front-brand__name {
    font-family: "Fira Sans", sans-serif;
    font-weight: 400;
    font-size: 36px;
    color: var(--white);
    letter-spacing: 0.2px;
  }

  .back-mark {
    position: absolute;
    left: 69px; top: 131px;
    width: 150px; height: 150px;
    border-radius: 50%;
    background: var(--brand-purple);
  }
  .name-band {
    position: absolute;
    left: 252px; top: 93px;
    width: 424px; height: 32px;
    background: var(--brand-purple);
    color: var(--white);
    font-weight: 700;
    font-size: 17px;
    line-height: 32px;
    padding-left: 18px;
  }
  .service {
    position: absolute;
    left: 268px; top: 134px;
    font-weight: 700;
    font-size: 22px;
  }
  .person {
    position: absolute;
    left: 268px; top: 165px;
    font-weight: 400;
    font-size: 17px;
  }
  .contact {
    position: absolute;
    left: 270px; top: 204px;
    list-style: none;
    font-size: 17px;
    line-height: 22px;
  }
  .contact__item {
    display: flex;
    align-items: flex-start;
    gap: 9px;
    margin-bottom: 7px;
  }
  .contact__icon { width: 16px; height: 16px; margin-top: 4px; flex: none; }
</style>
</head>
<body>
  <section class="card card--front" aria-label="Business card front">
    <div class="front-brand">
      <span class="front-brand__dot"></span>
      <span class="front-brand__name">Tranquilly Balanced Restoration</span>
    </div>
  </section>

  <section class="card card--back" aria-label="Business card back">
    <div class="back-mark"></div>
    <div class="name-band">Tranquilly Balanced Restoration</div>
    <h1 class="service">Mental health service</h1>
    <p class="person">Co-funder name</p>
    <ul class="contact">
      <li class="contact__item">
        <svg class="contact__icon" viewBox="0 0 16 16" aria-hidden="true">
          <circle cx="8" cy="8" r="8" fill="var(--brand-purple)"/>
          <path d="M5 4.2c.4-.3.8-.2 1 .2l.7 1.3c.2.4 0 .7-.3 1l-.4.3c.4 1 1.2 1.8 2.2 2.3l.3-.4c.3-.3.6-.5 1-.3l1.3.7c.4.2.5.6.2 1l-.5.6c-.5.5-1.3.6-2.1.2C6.5 10.3 5.1 8.8 4.4 7 4.1 6.2 4.2 5.4 4.7 4.9z" fill="var(--white)"/>
        </svg>
        <span>833-555-0187</span>
      </li>
      <li class="contact__item">
        <svg class="contact__icon" viewBox="0 0 16 16" aria-hidden="true" fill="none" stroke="var(--brand-purple)" stroke-width="1.1">
          <circle cx="8" cy="8" r="7"/>
          <ellipse cx="8" cy="8" rx="3" ry="7"/>
          <path d="M1 8h14M2 4.5h12M2 11.5h12"/>
        </svg>
        <span>www.tranquillybalanced.com</span>
      </li>
      <li class="contact__item">
        <svg class="contact__icon" viewBox="0 0 16 20" aria-hidden="true" style="height:20px">
          <path d="M8 0a6 6 0 0 1 6 6c0 4-6 11-6 11S2 10 2 6a6 6 0 0 1 6-6z" fill="var(--brand-purple)"/>
          <circle cx="8" cy="6" r="2.2" fill="var(--white)"/>
        </svg>
        <span>42 Meadowlark Lane, Suite 300,<br>Fairview, CO, United States, Colorado</span>
      </li>
    </ul>
  </section>
</body>
</html>
```